Company profile urgent

Hi, I had my designer fail to deliver and I am looking for urgent designers job. Needs to go to print tomorrow the latest. I need company profile designed and finished, I do have a start of the project but did not like the overall design as it was too simple and not something I would asking for. This needs to be a great job and we are willing to pay for the right job.

This is pretty much a folded brochure as you will see from the document that is attached. On the front side do not remove LOGO from the actual position as it must stay there for the purposes of the cover that is going over and it has a whole for the logo where it is. Also, the pages are set as it should be so do not change the order of the pages, only the design, feel and look. This is for a travel company needs to look expensive, upscale, vip and must have clean design.

Needs to be done:

.

Needs to be done:

1) Get the design more attractive and modern. Not looking for cheap but high quality material.
2) As you can see we are tryin to present 4 products in the brochure that we do and this will be a folded brochure.
3) Infographics, especially the table ''when to travel'' needs updates and more style
4) This design is very steril, we are looking for clean and modern design
5) On the front page add Company profile text somewhere and add any design on home page is welcome BUT logo must stay where is
6) Please send final print ready documents as well as editable so we can move the logo if needed as it must fit the whole on a brochure holder
7) Last page with contacts very poorly done by my designer, needs upgrade with maybe infographics for phone, email web etc... ideas welcome
8) if you need more photos at the end is link to photo bank

Ideas welcome! Again we need it fast and clean.

Photo bank:
https://files.example-share.net/f/q7Rm2LpX9vKt3NwB_hYe-uD4cZa-

Designes that we linked: https://layoutbazaar.example/item/company-profile-square-brochure/58203716?s_rank=8
https://layoutbazaar.example/item/company-profile_square/61937204?s_rank=32
https://layoutbazaar.example/item/square-brochure/64710392?s_rank=52

This is our webiste so you get the feeling of the colors: www.tramont-journeys.example

Important: Do not change text, or change pages, everything is as it should be just needs upgradede design! Logo on the first page must stay on the position as is.

Photo bank:

Target Market(s)

We are travel supplier targeting travel agents and travel companies

Industry/Entity Type

Travel Industry

Font styles to use
Serif
Sans Serif

Requirements
Must have
• https://files.example-share.net/f/q7Rm2LpX9vKt8pH_D3muWE5QbTokzr
Nice to have
• Cool design: https://layoutbazaar.example/item/business-solution-brochure-template/57382910?s_rank=3
• Cool design 2: https://layoutbazaar.example/item/travel-agency-catalog-brochure/57491836?s_rank=6
Should not have
• Do not change the dimensions. You have the design attached, indd file. Needs work and update.

```html
<!DOCTYPE html>
<html lang="en">
<head>
<meta charset="utf-8">
<title>Tramont Journeys – Company Profile Cover</title>
<link rel="stylesheet" href="https://fonts.googleapis.com/css2?family=Open+Sans:wght@400;600;800&display=swap">
<style>
  :root {
    --brand-red: #8c1520;
    --brand-red-deep: #700f19;
    --paper: #f5f5f5;
    --ink-white: #ffffff;
    --ink-grey: #6d6d6d;
    --spine-mark: #1d1d1d;
  }
  html, body {
    margin: 0;
    padding: 0;
    width: 1200px;
    height: 900px;
    overflow: hidden;
    background: var(--paper);
  }
  .cover {
    position: relative;
    width: 1200px;
    height: 900px;
    overflow: hidden;
    background: var(--paper);
    font-family: "Open Sans", Arial, sans-serif;
  }
  .cover-art {
    position: absolute;
    inset: 0;
  }
  .brand {
    position: absolute;
    left: 92px;
    top: 130px;
    color: var(--brand-red);
    line-height: 1;
  }
  .brand-name {
    display: block;
    font-size: 84px;
    font-weight: 800;
    letter-spacing: -1px;
  }
  .brand-sub {
    display: block;
    margin-top: 16px;
    font-size: 20px;
    font-weight: 800;
    letter-spacing: 30px;
    padding-left: 6px;
  }
  .doc-title {
    position: absolute;
    left: 95px;
    top: 306px;
    display: flex;
    align-items: center;
    gap: 14px;
    color: var(--ink-grey);
    font-size: 17px;
    font-weight: 600;
    letter-spacing: 6px;
  }
  .doc-title::before {
    content: "";
    width: 40px;
    height: 2px;
    background: var(--brand-red);
  }
  .tagline {
    position: absolute;
    left: 95px;
    top: 690px;
    color: var(--ink-white);
    line-height: 1.05;
  }
  .tagline-lead {
    display: block;
    font-size: 48px;
    font-weight: 800;
  }
  .tagline-rest {
    display: block;
    font-size: 38px;
    font-weight: 400;
  }
  .web {
    position: absolute;
    left: 98px;
    top: 822px;
    display: flex;
    align-items: center;
    gap: 10px;
    color: var(--ink-white);
    font-size: 21px;
  }
  .spine-mark {
    position: absolute;
    left: 0;
    top: 812px;
    width: 30px;
    height: 40px;
    background: var(--spine-mark);
  }
</style>
</head>
<body>
<main class="cover">
  <svg class="cover-art" width="1200" height="900" viewBox="0 0 1200 900">
    <defs>
      <linearGradient id="sea-gradient" x1="0" y1="0" x2="0.35" y2="1">
        <stop offset="0" stop-color="#f3ddd6"/>
        <stop offset="0.18" stop-color="#c9e3ea"/>
        <stop offset="0.4" stop-color="#4fb4d2"/>
        <stop offset="0.7" stop-color="#1f7fa8"/>
        <stop offset="1" stop-color="#173d52"/>
      </linearGradient>
      <radialGradient id="wake-glow" cx="0.45" cy="0.45" r="0.4">
        <stop offset="0" stop-color="#ffffff" stop-opacity="0.55"/>
        <stop offset="1" stop-color="#ffffff" stop-opacity="0"/>
      </radialGradient>
      <linearGradient id="falls-gradient" x1="0" y1="0" x2="1" y2="1">
        <stop offset="0" stop-color="#5d8a3a"/>
        <stop offset="0.5" stop-color="#a8b89c"/>
        <stop offset="1" stop-color="#3b5a2a"/>
      </linearGradient>
      <linearGradient id="old-town-gradient" x1="0" y1="0" x2="1" y2="1">
        <stop offset="0" stop-color="#2d6e98"/>
        <stop offset="0.5" stop-color="#a86a50"/>
        <stop offset="1" stop-color="#5a6e3a"/>
      </linearGradient>
      <linearGradient id="island-gradient" x1="0" y1="0" x2="0" y2="1">
        <stop offset="0" stop-color="#9cc8ea"/>
        <stop offset="0.35" stop-color="#2f5eae"/>
        <stop offset="0.65" stop-color="#3e7a3a"/>
        <stop offset="1" stop-color="#2e5a28"/>
      </linearGradient>
    </defs>

    <g class="hero-photo" role="img" aria-label="Photo: white motor yacht speeding across blue sea">
      <polygon points="620,0 1200,0 1200,900 430,900" fill="url(#sea-gradient)"/>
      <ellipse cx="860" cy="420" rx="300" ry="220" fill="url(#wake-glow)"/>
    </g>

    <polygon class="accent-band" points="0,455 700,900 0,900" fill="var(--brand-red)"/>
    <polygon class="accent-stripe" points="0,455 700,900 640,900 0,492" fill="var(--brand-red-deep)"/>

    <g class="tile" transform="translate(225 575) rotate(32)">
      <rect x="-80" y="-80" width="160" height="160" fill="#ffffff"/>
      <rect x="-74" y="-74" width="148" height="148" fill="url(#falls-gradient)" role="img" aria-label="Photo: waterfall among green moss"/>
    </g>

    <g class="tile" transform="translate(495 570) rotate(32)">
      <rect x="-105" y="-105" width="210" height="210" fill="url(#old-town-gradient)" role="img" aria-label="Photo: walled old town on the coast"/>
      <rect x="-92" y="-92" width="184" height="184" fill="none" stroke="#ffffff" stroke-width="1.5"/>
    </g>

    <g class="tile" transform="translate(705 750) rotate(32)">
      <rect x="-120" y="-120" width="240" height="240" fill="url(#island-gradient)" role="img" aria-label="Photo: green island bay with blue sea"/>
      <rect x="-106" y="-106" width="212" height="212" fill="none" stroke="#ffffff" stroke-width="1.5"/>
    </g>
  </svg>

  <div class="brand">
    <span class="brand-name">TRAMONT</span>
    <span class="brand-sub">JOURNEYS</span>
  </div>

  <div class="doc-title">COMPANY PROFILE</div>

  <div class="tagline">
    <span class="tagline-lead">YOUR</span>
    <span class="tagline-rest">TAGLINE HERE</span>
  </div>

  <div class="web">
    <svg width="20" height="20" viewBox="0 0 20 20" aria-hidden="true">
      <g fill="none" stroke="#ffffff" stroke-width="1.4">
        <circle cx="10" cy="10" r="8"/>
        <ellipse cx="10" cy="10" rx="3.5" ry="8"/>
        <line x1="2" y1="10" x2="18" y2="10"/>
      </g>
    </svg>
    <span>www.tramont-journeys.example</span>
  </div>

  <div class="spine-mark"></div>
</main>
</body>
</html>
```